Quantity Surveying Company Marketing Material

We need a flyer design, Three fold A4 (A4 sheet folded to 3) Two sides
Company: Varnel Advisory Pty Ltd,
Chartered Quantity Surveyors, Tax Depreciation Consultants
Services: Cost Planning, Estimating, Tax Depreciation, Expert Witness, Bills of Quantities, Tenders, Contract Administration
Highlights: Highly professional service, qualified and experienced staff, quality of service and accuracy
Our motto: Quality service at an affordable price
Our theme: Your partner in construction cost management
Company colour scheme: Blue
Website: www.varneladvisory-example.com.au

Target Market(s)

Architects, Builders, Construction companies, Home owner builders, Investment property owners (Mainly Residential projects such as houses, townhouses, apartments. In addition Retail and Civil infrastructure projects)

Industry/Entity Type

It Company

Colors
3176b5
886aae
33b8a4
fac994

Requirements
Must have
• Senior staff are
• Professional members of Imperial Guild of Licensed Assessors (IGLA)
• Professional members of National Society of Building Estimators (NSBE)
• Professional members of Federated College of Erectors (FCOE)
• Registered members of Levy Agents Council (LAC)
• (If this is too wordy, short form names with logos will suffice. But I do not have the FCOE logo)
Nice to have
• Blue and purple colours
• Above mentioned IGLA logo, NSBE logo and LAC logo
Should not have
• No to any funny stuff non-professional stuff.

```html
<!DOCTYPE html>
<html lang="en">
<head>
<meta charset="utf-8">
<title>Varnel Advisory Pty Ltd – Services</title>
<link rel="stylesheet" href="https://fonts.googleapis.com/css2?family=Fira+Sans+Extra+Condensed:wght@500;600&display=swap">
<style>
  :root {
    --blue: #2f6fb6;
    --purple: #7a62ad;
    --teal: #33b8a4;
    --peach: #fac994;
    --ink: #1b1c48;
    --frame: #111111;
    --paper: #ffffff;
  }
  * { margin: 0; padding: 0; box-sizing: border-box; }
  html, body {
    width: 1200px; height: 1000px; overflow: hidden;
    background: var(--paper);
    font-family: "Fira Sans Extra Condensed", "Arial Narrow", sans-serif;
    font-weight: 600;
  }
  .spread {
    position: absolute; left: 0; top: 76px; width: 1200px; height: 851px;
    border-top: 2px solid var(--frame);
    border-bottom: 2px solid var(--frame);
    border-left: 1px solid var(--frame);
    border-right: 1px solid var(--frame);
    overflow: hidden;
  }
  .skyline {
    position: absolute; left: 0; right: 0; bottom: 0; height: 120px;
    background: linear-gradient(90deg, #eceaf4 0%, #c3b8db 22%, #d9c3cf 40%, #f8dcc0 52%, #d8e2c6 68%, #a8dccf 85%, #8edbcd 100%);
    opacity: .9;
  }
  .sectors { position: absolute; left: 28px; top: 22px; width: 380px; color: var(--blue); }
  .heading { color: var(--purple); font-size: 28px; font-weight: 600; }
  .sectors .intro { margin-top: 20px; font-size: 18px; line-height: 24px; }
  .sector-list { list-style: none; margin-top: 14px; }
  .sector-list li { position: relative; font-size: 18px; line-height: 24px; margin-bottom: 24px; white-space: nowrap; }
  .sector-list li::before {
    content: ""; position: absolute; left: -11px; top: 9px; width: 6px; height: 6px;
    border-radius: 50%; background: var(--purple);
  }
  .services { position: absolute; left: 432px; top: 14px; width: 750px; color: var(--ink); }
  .subhead { font-size: 20px; margin-top: 16px; }
  .subhead.teal { color: var(--teal); }
  .subhead.peach { color: var(--peach); margin-top: 24px; }
  .services .intro { margin-top: 26px; font-size: 18px; line-height: 24px; }
  .service-list, .promise-list { list-style: none; font-size: 18px; line-height: 24px; }
  .service-list { margin-top: 24px; }
  .promise-list { margin-top: 26px; }
  .service-list li, .promise-list li { position: relative; white-space: nowrap; }
  .service-list li::before, .promise-list li::before {
    content: ""; position: absolute; left: -9px; top: 12px; width: 5px; height: 5px; border-radius: 50%;
  }
  .service-list li::before { background: var(--teal); }
  .promise-list li::before { background: var(--peach); top: 9px; }
  .detail { display: block; }
</style>
</head>
<body>
<main class="spread">
  <div class="skyline" role="img" aria-label="Soft pastel city skyline silhouette fading from lilac through peach to teal"></div>

  <section class="sectors">
    <h2 class="heading">Our industry sectors:</h2>
    <p class="intro">We have a broad range of experience in a number<br>sectors in the construction industry. We are currently<br>focussing on and specialising in:</p>
    <ul class="sector-list">
      <li>Residential: Houses, Townhouses, Apartments</li>
      <li>Retail: Malls, Cafés, Bars, Restaurants</li>
      <li>Commercial: Offices, Commercial buildings, Fit-out</li>
      <li>Civil Engineering: Roads, Car parks, Landscaping</li>
      <li>Renovations, Extensions, Upgrading</li>
    </ul>
  </section>

  <section class="services">
    <h2 class="heading">What we do:</h2>
    <h3 class="subhead teal">OUR SPECIALIST SERVICES</h3>
    <p class="intro">We provide highest quality service at an affordable price. Our services include:</p>
    <ul class="service-list">
      <li>Cost Planning, Estimating<span class="detail">(Budget estimates, DA Estimates, Elemental cost plans, Detailed cost plans, Life cycle cost assessments,<br>Sinking fund forecast, Replacement cost estimates, Bid preparation)</span></li>
      <li>Bills of Quantities,<span class="detail">(Client side bills of quantities, Builder’s quantities)</span></li>
      <li>Tax Depreciation, QS Reports<span class="detail">(Tax depreciation and capital allowance schedules and reports)</span></li>
      <li>Expert Witness<span class="detail">(Expert reports, Scott schedules, Expert opinion evidence)</span></li>
      <li>Contract Administration<span class="detail">(Valuations, Variations, Claims)</span></li>
      <li>Tenders, Cost Analysis, Database Management<span class="detail">(Tender analysis, Cost Analysis, Databases)</span></li>
    </ul>
    <h3 class="subhead peach">WHAT YOU CAN EXPECT FROM US</h3>
    <ul class="promise-list">
      <li>High quality bespoke services provided by experienced and professionally qualified Quantity Surveyors.</li>
      <li>Appreciation of our Clients’ needs and expectations</li>
      <li>Affordable fees.</li>
      <li>Turnaround time aligned to our Client’s schedule.</li>
      <li>We work collaboratively with our Clients to achieve the best outcomes.</li>
    </ul>
  </section>
</main>
</body>
</html>
```